I need men clothes and shoes selling website

I am a running a small and medium scale business in the United States with deals on the sales of clothes and shoes for men. I am looking for a top quality website to project my business and activities i am relatively new into it. There will be categories for Jeans, Polo, T-shirt, Long sleeves, Short Leaves, sandals, shoes, and slippers. Users would be able to sort category by designers, color and size. I carryout my sales online and only ship to United States and Canada. My website by the name - brondel. I require creativity in the design of the website.

Business

Coded - Design and coding required

```html
<!DOCTYPE html>
<html lang="en">
<head>
<meta charset="utf-8">
<title>Brondel — Men's Clothing &amp; Shoes</title>
<link rel="stylesheet" href="https://fonts.googleapis.com/css2?family=Montserrat:wght@400;600;700&family=Open+Sans:wght@400;600&family=Raleway:wght@300;400;800&family=Amatic+SC:wght@700&display=swap">
<style>
  :root {
    --red: #e8242a;
    --pink: #ee4f5c;
    --bronze: #c2844c;
    --ink: #1f1f1f;
    --text: #333333;
    --muted: #8b8b8b;
    --line: #e3e3e3;
    --hero-light: #eeedef;
    --hero-dark: #d9d8dc;
    --card: #f3f3f3;
    --footer: #262626;
    --footer-text: #b8b8b8;
    --star: #f5b50a;
    --star-off: #cccccc;
  }
  * { box-sizing: border-box; margin: 0; padding: 0; }
  html, body { width: 1200px; height: 2605px; overflow: hidden; background: #fff; }
  body { font-family: "Open Sans", Arial, sans-serif; color: var(--text); }
  .page { position: relative; width: 1200px; height: 2605px; overflow: hidden; }
  .abs { position: absolute; }

  /* Top bar */
  .topbar { left: 0; top: 0; width: 1200px; height: 26px; border-bottom: 1px solid var(--line); font-size: 9px; color: var(--muted); }
  .topbar .welcome { position: absolute; left: 62px; top: 7px; }
  .topbar .links { position: absolute; right: 60px; top: 7px; display: flex; gap: 22px; }

  /* Header */
  .logo { left: 60px; top: 74px; display: flex; align-items: center; gap: 10px; }
  .logo .mark { width: 34px; height: 34px; background: var(--red); }
  .logo .name { font-family: "Montserrat", sans-serif; font-weight: 700; font-size: 30px; letter-spacing: 2px; color: var(--ink); }
  .header-icons { right: 72px; top: 60px; display: flex; gap: 20px; align-items: center; }
  .cart { position: relative; }
  .cart .badge { position: absolute; right: -9px; top: -8px; width: 14px; height: 14px; border-radius: 50%; background: var(--red); color: #fff; font-size: 8px; line-height: 14px; text-align: center; }
  .nav { right: 59px; top: 97px; display: flex; gap: 0; font-family: "Montserrat", sans-serif; font-weight: 600; font-size: 12px; color: var(--ink); }
  .nav a { display: block; height: 30px; line-height: 30px; padding: 0 11px; margin-left: 12px; text-decoration: none; color: inherit; }
  .nav a.active { background: var(--red); color: #fff; }

  /* Hero */
  .hero { left: 0; top: 167px; width: 1200px; height: 576px; }
  .hero-text { left: 394px; top: 368px; width: 458px; text-align: center; color: #fff; }
  .hero-text .kicker { font-family: "Montserrat", sans-serif; font-size: 12px; letter-spacing: 5px; font-weight: 600; }
  .hero-text .title { font-family: "Amatic SC", cursive; font-size: 92px; line-height: 1; margin-top: 6px; }

  /* Category tiles */
  .tile { top: 790px; height: 334px; overflow: hidden; }
  .tile .label { position: absolute; left: 0; right: 0; text-align: center; color: #fff; font-family: "Montserrat", sans-serif; }
  .tile .small { font-size: 18px; letter-spacing: 2px; font-weight: 400; }
  .tile .big { font-size: 26px; letter-spacing: 3px; font-weight: 700; line-height: 1.2; }

  /* Featured */
  .section-title { left: 61px; top: 1184px; width: 1078px; height: 28px; }
  .section-title h2 { position: absolute; left: 0; right: 0; text-align: center; font-family: "Montserrat", sans-serif; font-weight: 700; font-size: 20px; letter-spacing: 0.5px; color: var(--ink); top: 0; }
  .product { top: 1247px; width: 248px; }
  .product .photo { position: relative; height: 320px; border: 1px solid var(--line); overflow: hidden; }
  .product .name { text-align: center; font-family: "Montserrat", sans-serif; font-weight: 600; font-size: 11px; color: var(--ink); margin-top: 13px; }
  .product .stars { text-align: center; font-size: 13px; letter-spacing: 2px; margin-top: 5px; }
  .on { color: var(--star); } .off { color: var(--star-off); }
  .tag { position: absolute; right: 18px; top: 18px; width: 50px; height: 50px; }
  .tag span { position: absolute; inset: 0; display: flex; align-items: center; justify-content: center; color: #fff; font-family: "Montserrat", sans-serif; font-weight: 700; font-size: 10px; }
  .overlay { position: absolute; inset: 0; background: rgba(70,70,70,0.55); }
  .overlay .price { position: absolute; left: 0; right: 0; top: 140px; text-align: center; color: #fff; font-family: "Montserrat", sans-serif; font-weight: 700; font-size: 22px; }
  .overlay .was { position: absolute; left: 0; right: 0; top: 170px; text-align: center; color: #fff; font-family: "Montserrat", sans-serif; font-size: 13px; text-decoration: line-through; }
  .overlay .actions { position: absolute; left: 12px; right: 12px; bottom: 20px; height: 32px; border-top: 1px solid rgba(255,255,255,.7); display: flex; align-items: center; color: #fff; font-family: "Montserrat", sans-serif; font-weight: 700; font-size: 10px; }
  .overlay .actions .add { flex: 1; padding-left: 4px; }
  .overlay .actions .icon { width: 32px; height: 32px; border-left: 1px solid rgba(255,255,255,.7); display: flex; align-items: center; justify-content: center; }
  .arrow { top: 1382px; width: 32px; height: 32px; background: #2c2c2c; display: flex; align-items: center; justify-content: center; }

  /* Summer banner */
  .summer { left: 0; top: 1672px; width: 1200px; height: 362px; }
  .summer-text { left: 300px; top: 1746px; width: 600px; text-align: center; }
  .summer-text .line1 { font-family: "Raleway", sans-serif; font-weight: 300; font-size: 29px; color: var(--ink); letter-spacing: 0.5px; }
  .summer-text .line1 b { font-weight: 800; }
  .summer-text .line2 { margin-top: 8px; display: flex; justify-content: center; align-items: center; gap: 12px; }
  .summer-text .start { font-family: "Raleway", sans-serif; font-weight: 300; font-size: 64px; color: var(--ink); line-height: 1; letter-spacing: 1px; }
  .summer-text .price { background: var(--pink); color: #fff; font-family: "Montserrat", sans-serif; font-weight: 700; font-size: 56px; line-height: 82px; padding: 0 10px; }
  .btn-shop { left: 465px; top: 1889px; width: 204px; height: 46px; border: 2px solid var(--ink); font-family: "Montserrat", sans-serif; font-weight: 600; font-size: 15px; text-align: center; line-height: 42px; color: var(--ink); }

  /* Promo boxes */
  .promo { top: 2108px; width: 342px; height: 156px; border: 2px solid #d0d0d0; text-align: center; padding-top: 30px; }
  .promo .head { font-family: "Amatic SC", cursive; font-size: 58px; line-height: 1; }
  .promo .sub { font-family: "Open Sans", sans-serif; font-size: 19px; color: #b5b5b5; margin-top: 2px; }
  .promo.gift .head { color: #b0b0b0; }
  .promo.save { border-color: #e07a82; }
  .promo.save .head { color: #d4243a; }
  .promo.save .sub { color: #e06474; }
  .promo.ret { border-color: #444; }
  .promo.ret .head { color: var(--ink); }

  /* Footer */
  .footer { left: 0; top: 2331px; width: 1200px; height: 274px; background: var(--footer); color: var(--footer-text); }
  .footer .col { position: absolute; top: 42px; }
  .footer h3 { font-family: "Open Sans", sans-serif; font-weight: 400; font-size: 21px; color: #fff; margin-bottom: 12px; letter-spacing: 0.5px; }
  .footer ul { list-style: none; font-size: 12px; line-height: 28px; padding-left: 2px; }
  .footer .rule { position: absolute; left: 61px; right: 61px; top: 227px; height: 1px; background: #3c3c3c; }
  .footer .copy { position: absolute; left: 61px; top: 242px; font-size: 9px; color: #ddd; font-weight: 600; }
  .footer .pay { position: absolute; right: 59px; top: 236px; display: flex; gap: 7px; }
  .footer .pay span { width: 38px; height: 25px; background: #d9d9d9; border-radius: 2px; }
</style>
</head>
<body>
<div class="page">

  <div class="abs topbar">
    <div class="welcome">Default welcome msg!</div>
    <div class="links">
      <span>USD ⌄</span><span>English ⌄</span><span>My Account</span><span>Wish List (0)</span><span>Shopping Cart</span><span>Checkout</span>
    </div>
  </div>

  <div class="abs logo"><span class="mark"></span><span class="name">BRONDEL</span></div>

  <div class="abs header-icons">
    <svg width="13" height="13" viewBox="0 0 13 13"><circle cx="5.5" cy="5.5" r="4" fill="none" stroke="#222" stroke-width="2"/><line x1="8.5" y1="8.5" x2="12" y2="12" stroke="#222" stroke-width="2"/></svg>
    <span class="cart">
      <svg width="14" height="13" viewBox="0 0 14 13"><path d="M0 1h3l2 7h7l2-5H4" fill="none" stroke="#222" stroke-width="1.6"/><circle cx="6" cy="11" r="1.3" fill="#222"/><circle cx="11" cy="11" r="1.3" fill="#222"/></svg>
      <span class="badge">0</span>
    </span>
  </div>

  <nav class="abs nav">
    <a class="active">HOME</a><a>ABOUT US</a><a>MEN'S SHOES</a><a>MEN'S SHIRTS</a><a>MEN'S TSHIRTS</a><a>CONTACT US</a>
  </nav>

  <!-- Hero -->
  <svg class="abs hero" viewBox="0 0 1200 576">
    <rect width="1200" height="576" fill="var(--hero-light)"/>
    <polygon points="1200,0 1200,576 310,576 1030,0" fill="var(--hero-dark)"/>
    <rect x="88" y="0" width="262" height="576" fill="url(#p1)" role="img" aria-label="Photo of a man in a dark polo shirt, braces and light blue jeans"/>
    <rect x="892" y="6" width="256" height="570" fill="url(#p2)" role="img" aria-label="Photo of a young man in a grey polo shirt and a cap"/>
    <polygon points="622,47 851,276 622,505 393,276" fill="none" stroke="#555" stroke-width="1.5"/>
    <polygon points="622,72 826,276 622,480 418,276" fill="none" stroke="#aaa" stroke-width="1"/>
    <polygon points="622,108 790,276 622,444 454,276" fill="#262626"/>
    <line x1="520" y1="349" x2="724" y2="349" stroke="#fff" stroke-width="1"/>
    <defs>
      <linearGradient id="p1" x1="0" y1="0" x2="0" y2="1"><stop offset="0" stop-color="#4a4a4c"/><stop offset=".55" stop-color="#3c3d40"/><stop offset=".6" stop-color="#7ea6b8"/><stop offset="1" stop-color="#6f98ab"/></linearGradient>
      <linearGradient id="p2" x1="0" y1="0" x2="0" y2="1"><stop offset="0" stop-color="#a89e96"/><stop offset=".3" stop-color="#9c9b97"/><stop offset="1" stop-color="#8c8b88"/></linearGradient>
    </defs>
  </svg>
  <div class="abs hero-text">
    <div class="kicker">COLLECTION 2015</div>
    <div class="title">MEN'S</div>
  </div>

  <!-- Category tiles -->
  <div class="abs tile" style="left:61px;width:248px;background:linear-gradient(180deg,#6e6e6e,#2a2a2c 45%,#232325);" role="img" aria-label="Photo of a man in a black blazer">
    <div class="label" style="top:158px"><div class="small">NEW ARRIVALS</div><div class="big">MEN<br>JACKETS</div></div>
  </div>
  <div class="abs tile" style="left:337px;width:526px;background:linear-gradient(160deg,#8d8c8a,#5e5c59 55%,#4a4540);" role="img" aria-label="Photo of a man rolling up his trousers above a white loafer on a street">
    <div class="label" style="top:200px;font-family:'Raleway',sans-serif;font-weight:300;font-size:72px;letter-spacing:6px;color:rgba(255,255,255,.45);left:150px;right:auto">STREET</div>
    <div class="label" style="top:222px;left:150px;right:auto;width:320px;font-size:26px;letter-spacing:3px;font-weight:700">COLLECTION</div>
  </div>
  <div class="abs tile" style="left:891px;width:248px;background:linear-gradient(180deg,#6e6e6e,#2a2a2c 45%,#232325);" role="img" aria-label="Photo of a man in a black blazer">
    <div class="label" style="top:158px"><div class="small">NEW ARRIVALS</div><div class="big">MEN<br>JACKETS</div></div>
  </div>

  <!-- Featured products -->
  <div class="abs section-title">
    <svg width="1078" height="28" style="position:absolute;left:0;top:0">
      <line x1="0" y1="14" x2="360" y2="14" stroke="var(--line)"/>
      <polygon points="388,9 393,14 388,19 383,14" fill="none" stroke="#999"/>
      <polygon points="690,9 695,14 690,19 685,14" fill="none" stroke="#999"/>
      <line x1="718" y1="14" x2="1078" y2="14" stroke="var(--line)"/>
    </svg>
    <h2>FEATURED PRODUCTS</h2>
  </div>

  <div class="abs arrow" style="left:46px"><svg width="8" height="10"><path d="M6 1L2 5l4 4" fill="none" stroke="#fff" stroke-width="1.6"/></svg></div>
  <div class="abs arrow" style="left:1124px"><svg width="8" height="10"><path d="M2 1l4 4-4 4" fill="none" stroke="#fff" stroke-width="1.6"/></svg></div>

  <div class="abs product" style="left:61px">
    <div class="photo" role="img" aria-label="Product photo: man in a denim jacket and patterned shorts" style="background:linear-gradient(180deg,var(--card),#c9d3dc 35%,#56627a 65%,var(--card) 90%)">
      <div class="tag"><svg width="50" height="50"><polygon points="25,0 50,25 25,50 0,25" fill="var(--red)"/></svg><span>SALE</span></div>
    </div>
    <div class="name">CRAS NEQUE METUS</div>
    <div class="stars"><span class="on">★★★★</span><span class="off">★</span></div>
  </div>

  <div class="abs product" style="left:339px">
    <div class="photo" role="img" aria-label="Product photo: man in a grey t-shirt and printed navy shorts" style="background:linear-gradient(180deg,var(--card),#d8d8d6 35%,#2b3044 65%,var(--card) 90%)">
      <div class="tag"><svg width="50" height="50"><polygon points="25,0 50,25 25,50 0,25" fill="var(--red)"/></svg><span>SALE</span></div>
    </div>
    <div class="name">NULLA LUCTUS MALESUADA</div>
    <div class="stars"><span class="off">★★★★★</span></div>
  </div>

  <div class="abs product" style="left:616px">
    <div class="photo" role="img" aria-label="Product photo: man in a black bomber jacket and grey shorts" style="background:linear-gradient(180deg,var(--card),#2a2a2c 35%,#7d7d7d 65%,var(--card) 90%)">
      <div class="tag"><svg width="50" height="50"><polygon points="25,0 50,25 25,50 0,25" fill="var(--bronze)"/></svg><span>NEW</span></div>
    </div>
    <div class="name">ETIAM GRAVIDA</div>
    <div class="stars"><span class="on">★★★★</span><span class="off">★</span></div>
  </div>

  <div class="abs product" style="left:893px">
    <div class="photo" role="img" aria-label="Product photo: man in a grey t-shirt and printed shorts" style="background:linear-gradient(180deg,#c8c8c8,#b4b4b2 35%,#2b3044 65%,#c8c8c8 90%)">
      <div class="overlay">
        <svg width="248" height="320" style="position:absolute;left:0;top:0"><polygon points="124,90 194,160 124,230 54,160" fill="none" stroke="#fff" stroke-width="1.5"/></svg>
        <div class="price">$100.00</div>
        <div class="was">$300.00</div>
        <div class="actions">
          <span class="add">ADD TO CART</span>
          <span class="icon"><svg width="12" height="11"><path d="M6 10L1.5 5.5A2.6 2.6 0 016 2a2.6 2.6 0 014.5 3.5z" fill="none" stroke="#fff" stroke-width="1.3"/></svg></span>
          <span class="icon"><svg width="12" height="10"><path d="M0 3h11M8 0l3 3M12 7H1M4 10L1 7" fill="none" stroke="#fff" stroke-width="1.3"/></svg></span>
          <span class="icon"><svg width="11" height="11"><circle cx="4.5" cy="4.5" r="3.3" fill="none" stroke="#fff" stroke-width="1.5"/><line x1="7" y1="7" x2="10.5" y2="10.5" stroke="#fff" stroke-width="1.6"/></svg></span>
        </div>
      </div>
      <div class="tag"><svg width="50" height="50"><polygon points="25,0 50,25 25,50 0,25" fill="var(--red)"/></svg><span>SALE</span></div>
    </div>
    <div class="name">VOLUPTAS NULLA</div>
    <div class="stars"><span class="on">★★</span><span class="off">★★★</span></div>
  </div>

  <!-- Summer banner -->
  <svg class="abs summer" viewBox="0 0 1200 362">
    <rect width="1200" height="362" fill="var(--hero-light)"/>
    <polygon points="1200,0 1200,362 360,362 760,0" fill="var(--hero-dark)"/>
    <rect x="70" y="0" width="270" height="362" fill="url(#s1)" role="img" aria-label="Photo of a bearded man in a white striped t-shirt"/>
    <rect x="790" y="0" width="322" height="362" fill="url(#s2)" role="img" aria-label="Photo of a bearded man in a white t-shirt with red sleeves and pocket"/>
    <defs>
      <linearGradient id="s1" x1="0" y1="0" x2="0" y2="1"><stop offset="0" stop-color="#8a6a55"/><stop offset=".4" stop-color="#c9a58e"/><stop offset=".55" stop-color="#f4f2ee"/><stop offset="1" stop-color="#ece9e4"/></linearGradient>
      <linearGradient id="s2" x1="0" y1="0" x2="1" y2="0"><stop offset="0" stop-color="#e04a55"/><stop offset=".3" stop-color="#efe9e2"/><stop offset=".7" stop-color="#e8e2da"/><stop offset="1" stop-color="#e04a55"/></linearGradient>
    </defs>
  </svg>
  <div class="abs summer-text">
    <div class="line1">NEW SUMMER <b>COLLECTION</b></div>
    <div class="line2"><span class="start">START AT</span><span class="price">$70.00</span></div>
  </div>
  <div class="abs btn-shop">SHOPPING NOW</div>

  <!-- Promo boxes -->
  <div class="abs promo gift" style="left:61px"><div class="head">Special gift cards</div><div class="sub">give the perfect gift</div></div>
  <div class="abs promo save" style="left:429px"><div class="head">Shop &amp; save</div><div class="sub">on all clothes</div></div>
  <div class="abs promo ret" style="left:797px"><div class="head">Order return</div><div class="sub">Returns within 14 days</div></div>

  <!-- Footer -->
  <footer class="abs footer">
    <div class="col" style="left:82px"><h3>ABOUT US</h3><ul><li>Wish List</li><li>Newsletter</li><li>Site Map</li><li>Affiliates</li><li>Contact Us</li></ul></div>
    <div class="col" style="left:358px"><h3>QUICK LINKS</h3><ul><li>Contact Us</li><li>Returns</li><li>Site Map</li><li>Affiliates</li><li>Wish List</li></ul></div>
    <div class="col" style="left:636px"><h3>SERVICES</h3><ul><li>Brands</li><li>Gift Vouchers</li><li>Wish List</li><li>Affiliates</li><li>Specials</li></ul></div>
    <div class="col" style="left:912px"><h3>CONTACT US</h3><ul><li>Contact Us</li><li>Order History</li><li>Wish List</li><li>Newsletter</li><li>Contact Us</li></ul></div>
    <div class="rule"></div>
    <div class="copy">© 2016 COPYRIGHT BRONDEL.COM</div>
    <div class="pay"><span></span><span></span><span></span><span></span><span></span></div>
  </footer>

</div>
</body>
</html>
```